Ridgeline Journeys business card

please see website
www.ridgelinejourneys.comau

info needed on card
Kieran Folsby
Ph
email
Adventure Riding GPS trails

please use my logo and colours off my site

Industry/Entity Type

Business

Contact Information for Business Card

Kieran Folsby
kieran@ridgelinejourneys.com

```html
<!DOCTYPE html>
<html lang="en">
<head>
<meta charset="utf-8">
<title>Ridgeline Journeys – Business Card</title>
<link rel="stylesheet" href="https://fonts.googleapis.com/css2?family=Roboto:wght@400;500;700&display=swap">
<style>
  :root {
    --stage: #232323;
    --card-black: #0b0b0b;
    --card-white: #ffffff;
    --accent: #f5d90a;
    --ink: #111111;
    --muted: #6f6f6f;
    --soft: #e8e8e8;
  }
  * { box-sizing: border-box; margin: 0; padding: 0; }
  html, body {
    width: 1200px; height: 750px; overflow: hidden;
    background: var(--stage);
    font-family: "Roboto", Arial, sans-serif;
  }
  .stage {
    position: relative; width: 1200px; height: 750px;
    display: flex; align-items: center; justify-content: center; gap: 60px;
  }
  .card {
    position: relative; width: 500px; height: 286px;
    box-shadow: 0 18px 40px rgba(0,0,0,.55);
    overflow: hidden;
  }

  /* Back of card */
  .card--back {
    background: radial-gradient(ellipse at 50% 40%, #222 0%, var(--card-black) 70%);
    display: flex; flex-direction: column; align-items: center; justify-content: center;
  }
  .brand-lockup { display: flex; align-items: center; gap: 12px; }
  .brand-dot { width: 22px; height: 22px; border-radius: 50%; background: var(--accent); }
  .card--back .brand-name {
    color: var(--soft); font-weight: 700; font-size: 30px; letter-spacing: .5px;
  }
  .card--back .tagline {
    margin-top: 18px; color: var(--soft); font-size: 13px; letter-spacing: .4px;
  }

  /* Front of card */
  .card--front { background: var(--card-white); }
  .card--front .brand-lockup {
    position: absolute; top: 34px; right: 30px; gap: 10px;
  }
  .card--front .brand-dot { width: 18px; height: 18px; }
  .card--front .brand-name {
    color: var(--ink); font-weight: 700; font-size: 22px; text-transform: uppercase; letter-spacing: .3px;
  }
  .name-band {
    position: absolute; left: 0; top: 96px; width: 300px; height: 52px;
    background: var(--card-black);
    display: flex; align-items: center; padding-left: 34px;
  }
  .name-band .person {
    color: var(--accent); font-weight: 500; font-size: 20px; letter-spacing: .3px;
  }
  .contact {
    position: absolute; left: 44px; bottom: 40px; list-style: none;
  }
  .contact li {
    display: flex; align-items: center; gap: 8px;
    color: var(--muted); font-size: 12px; line-height: 20px;
  }
  .contact svg { width: 13px; height: 13px; flex: none; }
  .contact .tagline-line { color: var(--muted); font-size: 14px; margin-top: 6px; padding-left: 0; letter-spacing: .4px; }
</style>
</head>
<body>
<main class="stage">
  <section class="card card--back" aria-label="Card back">
    <div class="brand-lockup">
      <span class="brand-dot"></span>
      <span class="brand-name">Ridgeline Journeys</span>
    </div>
    <p class="tagline">Adventure Riding GPS trails</p>
  </section>

  <section class="card card--front" aria-label="Card front">
    <div class="brand-lockup">
      <span class="brand-dot"></span>
      <span class="brand-name">Ridgeline Journeys</span>
    </div>
    <div class="name-band"><span class="person">Kieran Folsby</span></div>
    <ul class="contact">
      <li>
        <svg viewBox="0 0 16 16" aria-hidden="true"><path fill="#f5d90a" d="M3.5 1.5l2.5 0 1 3.5-1.8 1.2a8 8 0 0 0 4.6 4.6L11 9l3.5 1v2.5c0 1-1 2-2 2A11 11 0 0 1 1.5 3.5c0-1 1-2 2-2z"/></svg>
        555 0142 7788
      </li>
      <li>
        <svg viewBox="0 0 16 16" aria-hidden="true"><rect x="1" y="3.5" width="14" height="9" rx="1" fill="#f5d90a"/><path d="M1.5 4l6.5 5 6.5-5" fill="none" stroke="#fff" stroke-width="1.3"/></svg>
        kieran@ridgelinejourneys.com
      </li>
      <li>
        <svg viewBox="0 0 16 16" aria-hidden="true"><circle cx="8" cy="8" r="7" fill="#f5d90a"/><path d="M1 8h14M8 1c-3 3.5-3 10.5 0 14M8 1c3 3.5 3 10.5 0 14" fill="none" stroke="#fff" stroke-width="1.1"/></svg>
        www.ridgelinejourneys.comau
      </li>
      <li class="tagline-line">Adventure Riding GPS trails</li>
    </ul>
  </section>
</main>
</body>
</html>
```